Marlow Realty Real Estate Brokerage Recruiting Flyer

We are a real estate brokerage looking to hire more real estate agents. We need to list everything we have to offer as a company so real estate agents will join our company. this is our company website: www.Marlowrealty.example .

100% COMMISSION NO MONTHLY FEE
$450 Flat Transaction FEE

What We Offer:
24/7 Office Access
Free E & O Insurance for 1st Year
Free Online CE and PLE
Free 1,000 Business Cards
Free Professional Social Media Marketing
Free Printing, Scanning, and Copies
Free Buyer and Seller Presentation Packages
Free Filquay Cloud Based Document Management Access
Access to our Internal Brokerage Forum
Company Profit Sharing!
Private Offices Available to Rent

*Lead Generation Software with over 3,000 Leads
*10 Leads to Start
* Free Personal CRM and Website
*Restrictions and Rules apply

Company Address:
4817 Amberfield Road
Suite 512
Fairfax, VA 22194
Phone: 703-555-0147
email: info@marlowrealty.example

Target Market(s)

Real Estate Agents

Industry/Entity Type

Real Estate

Colors
0555a3
ffffff

Requirements
Must have
• 100% COMMISSION NO MONTHLY FEE
$450 Flat Transaction FEE

What We Offer:
24/7 Office Access
Free Online CE and PLE
Free 1,000 Business Cards
Company Profit Sharing!

*10 Leads to Start

Company Address:
4817 Amberfield Road
Suite 512
Fairfax, VA 22194
Phone: 703-555-0147

```html
<!DOCTYPE html>
<html lang="en">
<head>
<meta charset="utf-8">
<title>Marlow Realty – Agent Recruiting Flyer</title>
<link rel="stylesheet" href="https://fonts.googleapis.com/css2?family=Jost:wght@300;400;500;700;800&family=Arimo:wght@400;700&display=swap">
<style>
  :root {
    --navy: #1f3c7c;
    --navy-deep: #17306a;
    --red: #c8202a;
    --white: #ffffff;
    --ink: #1d1d1f;
    --band-grey: #d8d9db;
    --rule: #b9bcc4;
    --stage: #e4e4e4;
  }
  * { box-sizing: border-box; margin: 0; padding: 0; }
  html, body { width: 1200px; height: 900px; overflow: hidden; }
  body {
    background: var(--stage);
    font-family: "Arimo", Arial, sans-serif;
    color: var(--ink);
    position: relative;
  }
  .flyer {
    position: absolute;
    left: 282px; top: 0;
    width: 636px; height: 900px;
    background: var(--white);
    overflow: hidden;
  }
  .brand {
    position: absolute; left: 40px; top: 36px;
    display: flex; align-items: center; gap: 8px;
    font-family: "Jost", sans-serif; font-weight: 500;
    font-size: 20px; color: var(--navy); letter-spacing: .02em;
  }
  .brand-mark { width: 14px; height: 14px; background: var(--navy); }
  .license {
    position: absolute; right: 36px; top: 104px;
    font-family: "Jost", sans-serif; font-size: 11px; color: var(--ink);
  }
  .hero-photo {
    position: absolute; left: 0; top: 128px;
    width: 636px; height: 330px;
    background: linear-gradient(180deg, #6d8fbd 0%, #9fb0c8 38%, #7d6a5c 70%, #b7b5b2 100%);
  }
  .hero-panel {
    position: absolute; left: 0; top: 186px;
    width: 332px; height: 290px;
    background: rgba(27, 54, 116, .88);
  }
  .headline {
    position: absolute; left: 34px; top: 206px;
    font-family: "Jost", sans-serif; color: var(--white);
    text-transform: uppercase;
  }
  .headline-lead { font-weight: 300; font-size: 35px; line-height: 38px; display: block; }
  .headline-key { font-weight: 800; font-size: 50px; line-height: 48px; display: block; margin-top: 4px; }
  .offer-badge {
    position: absolute; left: 380px; top: 352px;
    width: 230px; height: 230px;
  }
  .offer-badge-text {
    position: absolute; inset: 0;
    display: flex; flex-direction: column; align-items: center; justify-content: center;
    font-family: "Jost", sans-serif; color: var(--white); text-align: center;
  }
  .badge-percent { font-weight: 800; font-size: 30px; line-height: 30px; }
  .badge-terms { font-weight: 700; font-size: 16px; line-height: 19px; }
  .badge-fee { font-weight: 400; font-size: 17px; line-height: 20px; margin-top: 10px; }
  .offer-heading {
    position: absolute; left: 40px; top: 494px;
    display: flex; align-items: center; gap: 12px;
    font-family: "Jost", sans-serif; font-weight: 700; font-size: 19px;
    color: var(--navy); text-transform: uppercase;
  }
  .offer-heading::after { content: ""; width: 150px; height: 1px; background: var(--rule); }
  .benefit-list { position: absolute; list-style: none; font-size: 13.5px; }
  .benefit-list li {
    display: flex; align-items: flex-start; gap: 10px;
    line-height: 17px; margin-bottom: 12px;
  }
  .benefit-list svg { flex: none; width: 13px; height: 13px; margin-top: 2px; }
  .benefits-left { left: 40px; top: 534px; width: 290px; }
  .benefits-right { left: 336px; top: 622px; width: 270px; }
  .perk-band {
    position: absolute; left: 0; top: 778px;
    width: 636px; height: 62px;
    background: var(--band-grey);
    display: grid; grid-template-columns: 1.35fr 1fr 1fr 1fr;
    align-items: center; text-align: center;
    font-size: 12.5px; line-height: 16px;
  }
  .perk-band span { padding: 0 8px; border-right: 1px solid var(--rule); }
  .perk-band span:last-child { border-right: none; }
  .contact-footer {
    position: absolute; left: 0; top: 840px;
    width: 636px; height: 60px;
    background: var(--navy);
    color: var(--white); text-align: center;
    font-size: 12.5px; line-height: 19px;
    display: flex; flex-direction: column; justify-content: center;
  }
  .contact-footer b { font-weight: 700; }
</style>
</head>
<body>
<main class="flyer">
  <header>
    <div class="brand"><span class="brand-mark"></span>Marlow Realty</div>
    <p class="license">Licensed in D.C., Maryland, and Virginia</p>
  </header>

  <div class="hero-photo" role="img" aria-label="Photo of a modern two-storey house with lit windows and garage at dusk, surrounded by pine trees"></div>
  <div class="hero-panel"></div>
  <h1 class="headline">
    <span class="headline-lead">One stop<br>solution<br>to all your</span>
    <span class="headline-key">Real estate<br>needs</span>
  </h1>

  <div class="offer-badge">
    <svg viewBox="-110 -110 220 220" width="230" height="230" aria-hidden="true">
      <polygon fill="#c8202a" points="100,0 87.2,11.5 96.6,25.9 81.3,33.7 86.6,50 69.8,53.6 70.7,70.7 53.6,69.8 50,86.6 33.7,81.3 25.9,96.6 11.5,87.2 0,100 -11.5,87.2 -25.9,96.6 -33.7,81.3 -50,86.6 -53.6,69.8 -70.7,70.7 -69.8,53.6 -86.6,50 -81.3,33.7 -96.6,25.9 -87.2,11.5 -100,0 -87.2,-11.5 -96.6,-25.9 -81.3,-33.7 -86.6,-50 -69.8,-53.6 -70.7,-70.7 -53.6,-69.8 -50,-86.6 -33.7,-81.3 -25.9,-96.6 -11.5,-87.2 0,-100 11.5,-87.2 25.9,-96.6 33.7,-81.3 50,-86.6 53.6,-69.8 70.7,-70.7 69.8,-53.6 86.6,-50 81.3,-33.7 96.6,-25.9 87.2,-11.5"/>
    </svg>
    <div class="offer-badge-text">
      <span class="badge-percent">100%</span>
      <span class="badge-terms">COMMISSION<br>NO MONTHLY FEE</span>
      <span class="badge-fee">$450 Flat<br>Transaction FEE</span>
    </div>
  </div>

  <h2 class="offer-heading">What we offer</h2>

  <svg width="0" height="0" style="position:absolute">
    <symbol id="tick" viewBox="0 0 14 14">
      <circle cx="7" cy="7" r="7" fill="#1f3c7c"/>
      <path d="M3.8 7.2 6.1 9.4 10.3 4.9" fill="none" stroke="#fff" stroke-width="1.7" stroke-linecap="round" stroke-linejoin="round"/>
    </symbol>
  </svg>

  <ul class="benefit-list benefits-left">
    <li><svg><use href="#tick"/></svg>24/7 Office Access</li>
    <li><svg><use href="#tick"/></svg>Free E &amp; O Insurance for 1st Year</li>
    <li><svg><use href="#tick"/></svg>Free Online CE and PLE</li>
    <li><svg><use href="#tick"/></svg>Free 1,000 Business Cards</li>
    <li><svg><use href="#tick"/></svg>Free Professional Social Media Marketing</li>
    <li><svg><use href="#tick"/></svg>Free Printing, Scanning, and Copies</li>
    <li><svg><use href="#tick"/></svg>Free Buyer and Seller Presentation Packages</li>
  </ul>

  <ul class="benefit-list benefits-right">
    <li><svg><use href="#tick"/></svg>Free Filquay Cloud Based Document Management Access</li>
    <li><svg><use href="#tick"/></svg>Access to our Internal Brokerage Forum</li>
    <li><svg><use href="#tick"/></svg>Company Profit Sharing!</li>
    <li><svg><use href="#tick"/></svg>Private Offices Available to Rent</li>
  </ul>

  <section class="perk-band">
    <span>Lead Generation Software<br>with over 3,000 Leads</span>
    <span>10 Leads to Start</span>
    <span>Free Personal CRM<br>and Website</span>
    <span>Restrictions and<br>Rules apply</span>
  </section>

  <footer class="contact-footer">
    <p><b>Address:</b> 4817 Amberfield Road, Suite 512, Fairfax, VA 22194</p>
    <p><b>Phone:</b> 703-555-0147 &nbsp;|&nbsp; <b>Email:</b> info@marlowrealty.example</p>
  </footer>
</main>
</body>
</html>
```